Solar Company Bussiness Card

I need a 2 sided business card and would like a .psd and any font files for each side of the card. I would like my logo used, it should be attached with the fonts. I'm not opposed to the font colors with the logo being changed.

On the sample design, I'd like the following:

Darren Pellow
President
Phone: 555-318-2947
www.sunvaleenergyco.example

As I've recently opened in a 2nd market, I'm not sure about an address as I currently have 2 of them. I may actually get separate cards printed, one batch for each address, that's why I need the PSD file.
Updates

I'm very pleased with the response and designs I've received here for my business card. First and foremost, I'd like to thank everyone who took the time to submit a design. There truly are a lot of great designs in the bunch here and I'm having a little difficulty deciding. I will be reaching out to someone in the next day or two here to go to a final design. At this time, I'm not looking for any new concepts. If any of you do logos, I'm looking for a new logo for our sister entity, Pellow Partners, Inc. Thanks, Darren Pellow

Reason: I'm not looking for any new designs at this point, but extending this deadline in order to give people I've asked a chance to re-submit items.

Industry/Entity Type

Business

```html
<!DOCTYPE html>
<html lang="en">
<head>
<meta charset="utf-8">
<title>Sunvale Energy – Business Card</title>
<link rel="stylesheet" href="https://fonts.googleapis.com/css2?family=Open+Sans:wght@400;600;700&display=swap">
<style>
  :root {
    --page: #ececea;
    --card: #ffffff;
    --slate: #2d383d;
    --slate-mid: #4f6468;
    --mint: #86e6d4;
    --mint-soft: #9cebdc;
    --brand-blue: #3ba4d6;
    --ink-white: #ffffff;
    --shadow: rgba(0, 0, 0, 0.28);
  }
  * { box-sizing: border-box; margin: 0; padding: 0; }
  html, body {
    width: 1200px;
    height: 960px;
    overflow: hidden;
    background: var(--page);
    font-family: "Open Sans", Arial, sans-serif;
  }
  .canvas { position: relative; width: 1200px; height: 960px; }
  .card {
    position: absolute;
    width: 600px;
    height: 350px;
    background: var(--card);
    box-shadow: 4px 6px 14px var(--shadow);
    overflow: hidden;
  }
  .card svg.card-art { position: absolute; inset: 0; width: 600px; height: 350px; }
  .card--front { left: 150px; top: 80px; }
  .card--back { left: 475px; top: 480px; }

  .brand {
    position: absolute;
    display: flex;
    align-items: center;
    color: var(--brand-blue);
    font-weight: 600;
    white-space: nowrap;
  }
  .brand__mark { background: var(--brand-blue); flex: none; }
  .brand--large { left: 78px; top: 142px; font-size: 46px; gap: 18px; }
  .brand--large .brand__mark { width: 46px; height: 46px; }
  .brand--small { left: 40px; top: 22px; font-size: 21px; gap: 9px; }
  .brand--small .brand__mark { width: 20px; height: 20px; }

  .contact {
    position: absolute;
    right: 46px;
    top: 120px;
    text-align: right;
    color: var(--ink-white);
  }
  .contact__name { font-size: 23px; font-weight: 700; line-height: 1.2; }
  .contact__title { font-size: 17px; font-weight: 400; margin-top: 2px; }
  .contact__phone { font-size: 22px; font-weight: 400; margin-top: 30px; }
  .contact__web { font-size: 23px; font-weight: 700; margin-top: 26px; }
</style>
</head>
<body>
<main class="canvas">

  <section class="card card--front" aria-label="Card front">
    <svg class="card-art" viewBox="0 0 600 350" aria-hidden="true">
      <defs>
        <linearGradient id="front-top" x1="0" x2="1" y1="0" y2="0">
          <stop offset="0" stop-color="var(--slate)"/>
          <stop offset="0.55" stop-color="var(--slate-mid)"/>
          <stop offset="1" stop-color="var(--mint)"/>
        </linearGradient>
        <linearGradient id="front-bottom" x1="0" x2="1" y1="0" y2="0">
          <stop offset="0" stop-color="var(--mint)"/>
          <stop offset="0.5" stop-color="var(--slate-mid)"/>
          <stop offset="1" stop-color="var(--slate)"/>
        </linearGradient>
      </defs>
      <path d="M0 0 H600 V42 C430 100 220 80 0 92 Z" fill="url(#front-top)"/>
      <path d="M0 305 C200 318 400 332 600 322 V350 H0 Z" fill="var(--mint-soft)"/>
      <path d="M0 300 C200 302 400 290 600 258 V322 C400 332 200 318 0 305 Z" fill="url(#front-bottom)"/>
    </svg>
    <div class="brand brand--large">
      <span class="brand__mark"></span>
      <span class="brand__name">Sunvale Energy</span>
    </div>
  </section>

  <section class="card card--back" aria-label="Card back">
    <svg class="card-art" viewBox="0 0 600 350" aria-hidden="true">
      <defs>
        <linearGradient id="back-field" x1="0" x2="1" y1="0" y2="0">
          <stop offset="0" stop-color="var(--mint)"/>
          <stop offset="0.5" stop-color="var(--slate-mid)"/>
          <stop offset="1" stop-color="var(--slate)"/>
        </linearGradient>
      </defs>
      <path d="M0 118 C110 150 220 140 320 100 C420 62 520 58 600 72 V350 H0 Z" fill="url(#back-field)"/>
      <path d="M0 118 C110 150 220 140 320 100 C420 62 520 58 600 72" fill="none" stroke="var(--slate)" stroke-width="3"/>
    </svg>
    <div class="brand brand--small">
      <span class="brand__mark"></span>
      <span class="brand__name">Sunvale Energy</span>
    </div>
    <div class="contact">
      <p class="contact__name">Darren Pellow</p>
      <p class="contact__title">President</p>
      <p class="contact__phone">555-318-2947</p>
      <p class="contact__web">www.sunvaleenergyco.example</p>
    </div>
  </section>

</main>
</body>
</html>
```